Australian Software Consultancy needs new Business Card Design

Design Business Card based on existing design artefacts (attached). We are open to all designs. As its a 2 sided design and we thought it might be quite striking to have one side with a black background and te other side with a white background.

Target Market(s)

Financial Services mainly.

Industry/Entity Type

Business

Contact Information for Business Card

Name :
Position :
Email :

Requirements
Must have
• Funky design using our existing assets

```html
<!DOCTYPE html>
<html lang="en">
<head>
<meta charset="utf-8">
<title>Keelstone Business Card</title>
<link rel="stylesheet" href="https://fonts.googleapis.com/css2?family=Montserrat:wght@400;500;600;700&display=swap">
<style>
  :root {
    --page: #ffffff;
    --ink: #000000;
    --paper: #ffffff;
    --accent: #e31e24;
    --edge: #bdbdbd;
  }
  * { margin: 0; padding: 0; box-sizing: border-box; }
  html, body {
    width: 1200px;
    height: 1000px;
    overflow: hidden;
    background: var(--page);
    font-family: "Montserrat", sans-serif;
  }
  .canvas { position: relative; width: 1200px; height: 1000px; }

  .card-front {
    position: absolute;
    left: 255px; top: 51px;
    width: 690px; height: 422px;
    background: var(--ink);
    display: flex;
    align-items: center;
    justify-content: center;
  }
  .front-brand {
    color: var(--accent);
    font-weight: 700;
    font-size: 30px;
    letter-spacing: 3px;
    text-transform: uppercase;
    margin-top: -20px;
  }

  .card-back {
    position: absolute;
    left: 254px; top: 540px;
    width: 690px; height: 423px;
    display: flex;
  }
  .identity-panel {
    position: relative;
    width: 345px; height: 100%;
    background: var(--ink);
  }
  .person-name {
    position: absolute;
    left: 54px; top: 188px;
    color: var(--paper);
    font-weight: 500;
    font-size: 19px;
    letter-spacing: 3.6px;
    white-space: nowrap;
  }
  .person-role {
    position: absolute;
    left: 54px; top: 215px;
    color: var(--accent);
    font-weight: 600;
    font-size: 13px;
    letter-spacing: 2px;
  }
  .contact-panel {
    position: relative;
    width: 345px; height: 100%;
    background: var(--paper);
    border: 1px solid var(--edge);
    border-left: none;
  }
  .contact-phone,
  .contact-email {
    position: absolute;
    left: 443px; left: 98px;
    color: var(--ink);
    font-weight: 500;
    font-size: 13px;
    letter-spacing: 2.6px;
    white-space: nowrap;
  }
  .contact-phone { top: 101px; }
  .contact-email { top: 308px; }
  .back-brand {
    position: absolute;
    left: 97px; top: 199px;
    color: var(--ink);
    font-weight: 700;
    font-size: 20px;
    letter-spacing: 0.5px;
    text-transform: uppercase;
  }
</style>
</head>
<body>
  <main class="canvas">
    <section class="card-front">
      <span class="front-brand">Keelstone</span>
    </section>

    <section class="card-back">
      <div class="identity-panel">
        <p class="person-name">YOUR NAME HERE</p>
        <p class="person-role">Positions</p>
      </div>
      <div class="contact-panel">
        <p class="contact-phone">+ 62 XXXX XXXX</p>
        <p class="back-brand">Keelstone</p>
        <p class="contact-email">email@mail.com</p>
      </div>
    </section>
  </main>
</body>
</html>
```